Business card design needed

We are a boutique law firm within the Melbourne CBD.

You will need to upload our company logo which is to go on the left hand side of the business card - we then have a Legal Guild of Carrowmere logo to go perhaps on the bottom right hand side (color)

On the back we would like the website details

www.hartwellsolicitors.com.au - with a small logo
Updates

Thank you designers for all your great submissions.  Just going through the designs and we will choose one within the next couple of days.

Kind Regards
Hartwells Solicitors Pty Ltd

Industry/Entity Type

Boutique

Contact Information for Business Card

Dominic Hartwell
Principal
Level 6, 47 Penrose Street
Melbourne VIC Australia 3000
T+61 3 9555 0142 F+61 3 9555 0187
dominic@hartwellsolicitors.com.au
M 0491 570 156

```html
<!DOCTYPE html>
<html lang="en">
<head>
<meta charset="utf-8">
<title>Hartwells Solicitors – Business Card</title>
<link rel="stylesheet" href="https://fonts.googleapis.com/css2?family=Arimo:wght@400;700&display=swap">
<style>
  :root {
    --backdrop: #e6e6e6;
    --ink: #0b0b0b;
    --paper: #f7f7f7;
    --white: #ffffff;
    --soft-text: #d8d8d8;
    --muted: #8a8a8a;
    --photo-dark: #050505;
    --photo-mid: #2a2a2a;
  }
  * { box-sizing: border-box; margin: 0; padding: 0; }
  html, body {
    width: 1200px; height: 1000px; overflow: hidden;
    background: var(--backdrop);
    font-family: "Arimo", Arial, sans-serif;
  }
  .canvas { position: relative; width: 1200px; height: 1000px; }

  .card {
    position: absolute; left: 250px; width: 700px; height: 428px;
    overflow: hidden;
    box-shadow: 0 6px 18px rgba(0,0,0,0.18);
  }
  .card--front { top: 60px; background: var(--ink); color: var(--white); }
  .card--back  { top: 520px; background: var(--paper); color: var(--ink); }

  /* front */
  .front-photo {
    position: absolute; inset: 0;
    background:
      radial-gradient(ellipse 55% 30% at 62% 42%, var(--photo-mid), transparent 70%),
      linear-gradient(180deg, #111 0%, var(--photo-dark) 55%, var(--ink) 100%);
  }
  .brand {
    position: absolute; display: flex; align-items: center; gap: 12px;
    font-weight: 700; color: var(--white); letter-spacing: -0.5px;
  }
  .brand__square { background: var(--white); flex: none; }
  .card--front .brand { left: 0; top: 150px; font-size: 46px; }
  .card--front .brand__square { width: 70px; height: 56px; }

  .guild-badge { position: absolute; right: 46px; top: 120px; width: 62px; height: 74px; }

  .contact {
    position: absolute; left: 40px; top: 248px;
    display: grid; grid-template-columns: 34px auto; row-gap: 4px;
    font-size: 17px; line-height: 22px; color: var(--soft-text);
  }
  .contact dt { font-weight: 700; color: var(--white); }

  .identity {
    position: absolute; left: 40px; top: 352px;
    font-size: 17px; line-height: 24px; color: var(--soft-text);
  }

  /* back */
  .web {
    position: absolute; left: 0; right: 0; top: 150px;
    display: flex; justify-content: center; align-items: center; gap: 14px;
    font-size: 20px; font-weight: 700; letter-spacing: 0.2px;
  }
  .web__cursor { width: 18px; height: 24px; }
  .back-band {
    position: absolute; left: 0; right: 0; bottom: 0; height: 118px;
    background: var(--ink);
  }
  .card--back .brand { left: 330px; top: 30px; font-size: 34px; }
  .card--back .brand__square { width: 48px; height: 40px; }
</style>
</head>
<body>
<div class="canvas">

  <section class="card card--front" aria-label="Business card front">
    <div class="front-photo" role="img" aria-label="Dark night-time photograph of a Melbourne city street with lit shopfront signs"></div>

    <div class="brand">
      <span class="brand__square"></span>
      <span class="brand__name">Hartwells</span>
    </div>

    <svg class="guild-badge" viewBox="0 0 62 74" role="img" aria-label="Legal Guild of Carrowmere badge">
      <path d="M4 4 H58 V36 C58 56 42 66 31 70 C20 66 4 56 4 36 Z" fill="#3a3a3a" stroke="#6a6a6a" stroke-width="2"/>
    </svg>

    <dl class="contact">
      <dt>T</dt><dd>+61 3 9555 0142</dd>
      <dt>F</dt><dd>+61 3 9555 0187</dd>
      <dt>E</dt><dd>dominic@hartwellsolicitors.com.au</dd>
      <dt>M</dt><dd>0491 570 156</dd>
    </dl>

    <div class="identity">
      <p>Dominic Hartwell Principal Hartwells Solicitors Pty Ltd</p>
      <p>Level 6, 47 Penrose Street Melbourne VIC Australia 3000</p>
    </div>
  </section>

  <section class="card card--back" aria-label="Business card back">
    <div class="web">
      <span class="web__url">http://www.hartwellsolicitors.com.au/</span>
      <svg class="web__cursor" viewBox="0 0 18 24" aria-hidden="true">
        <path d="M2 2 L2 19 L6.5 15 L10 22 L12.5 21 L9 14 L15 14 Z" fill="#ffffff" stroke="#111" stroke-width="1.4" stroke-linejoin="round"/>
      </svg>
    </div>

    <div class="back-band">
      <div class="brand">
        <span class="brand__square"></span>
        <span class="brand__name">Hartwells</span>
      </div>
    </div>
  </section>

</div>
</body>
</html>
```